Amazing Looking Flyer for Moving Services

This project is a bit special, so please read carefully.
I'm working with new online design system Plivora and need good designs based on that system.
You will be redesigning the attached ad/flyer using Plivora.
Here is my starting design but please do not use it because it didn't start good:
https://beta2.plivora-example.com/pub/tobiasm/DeskTidying

Please create the flyer in the size 1275x1650 pixels, for email and PDF and website.
This needs to be designed with Plivora so I can change it later.
You will need to register at plivora-example.com for this job but use only the free version there, do not pay for images or leave them watermarked and I'll pay later.

No logo is needed. Only text, better layout and some pictures.
Pictures can be from Plivora, or you can create some vector graphics, as I don't want to pay for other stock photos.

Note: when you do anything in Plivora you can click Publish, and after I choose and pay for design then you can publish again with option to make it editable by anyone. Then I will be able to take it and edit myself later.

Industry/Entity Type

Online

Requirements
Must have
• some graphics
• must be done in plivora for my editing later

```html
<!DOCTYPE html>
<html lang="en">
<head>
<meta charset="utf-8">
<title>Moving Solutions Flyer</title>
<link rel="stylesheet" href="https://fonts.googleapis.com/css2?family=Lato:ital,wght@0,400;0,700;0,900;1,700&family=Oswald:wght@400&display=swap">
<style>
  :root {
    --paper: #ffffff;
    --shape-grey: #e6e6e6;
    --ink: #111111;
    --accent-red: #b3242a;
    --ink-deep: #2a1515;
    --price-blue: #8396b2;
    --soft-blue: #9ba8bf;
    --muted: #555555;
    --dark-fade: #3a3a3a;
  }
  html, body { margin: 0; padding: 0; overflow: hidden; background: var(--paper); }
  .flyer {
    position: relative; width: 928px; height: 1200px; overflow: hidden;
    background: var(--paper); font-family: "Lato", sans-serif; color: var(--ink);
  }
  .shapes { position: absolute; inset: 0; }
  .block { position: absolute; margin: 0; line-height: 1; }
  .headline {
    right: 92px; top: 112px; text-align: right; font-weight: 400;
    font-size: 50px; line-height: 49px; letter-spacing: 0.5px;
  }
  .tagline {
    right: 92px; top: 214px; text-align: right; color: var(--accent-red);
    font-weight: 700; font-size: 27px; line-height: 36px;
  }
  .ribbon {
    left: 38px; top: 340px; transform: rotate(-45deg); transform-origin: left top;
    font-size: 23px; line-height: 24px; font-weight: 400; text-align: center; white-space: nowrap;
  }
  .ribbon span { display: block; }
  .condensed { font-family: "Oswald", sans-serif; font-weight: 400; }
  .we-move { left: 184px; width: 200px; top: 404px; text-align: center; }
  .list-head { font-size: 29px; line-height: 42px; }
  .list-item { font-size: 22px; line-height: 36px; }
  .we-provide { left: 500px; width: 180px; top: 408px; text-align: right; }
  .we-provide .list-head { text-align: center; line-height: 43px; }
  .drive {
    left: 731px; top: 420px; color: var(--accent-red); font-weight: 700;
    font-size: 26px; line-height: 27.5px;
  }
  .prices {
    left: 0; width: 928px; top: 724px; text-align: center;
    color: var(--price-blue); font-size: 29px; line-height: 38px;
  }
  .labor { left: 0; width: 928px; top: 860px; text-align: center; font-size: 20px; line-height: 30px; }
  .labor .rate { color: var(--price-blue); margin-bottom: 4px; display: block; }
  .labor .note { color: var(--muted); display: block; }
  .service {
    right: 259px; top: 990px; text-align: right; color: var(--ink-deep);
    font-weight: 700; font-size: 41px; line-height: 44px;
  }
  .tasks {
    left: 684px; top: 990px; color: var(--soft-blue); font-weight: 700;
    font-size: 29px; line-height: 34px;
  }
  .contact {
    left: 301px; top: 1146px; color: var(--muted); font-style: italic;
    font-weight: 700; font-size: 19px; word-spacing: 2px;
  }
  .contact span + span { margin-left: 22px; }
</style>
</head>
<body>
<div class="flyer">
  <svg class="shapes" width="928" height="1200" viewBox="0 0 928 1200" aria-hidden="true">
    <defs>
      <linearGradient id="edgeFade" x1="0" y1="0" x2="1" y2="0">
        <stop offset="0" stop-color="#2a2a2a"/>
        <stop offset="1" stop-color="#6a6a6a"/>
      </linearGradient>
    </defs>
    <polygon points="327,0 640,0 484,150" fill="var(--shape-grey)"/>
    <polygon points="928,145 858,215 928,284" fill="var(--ink)"/>
    <polygon points="291,203 524,436 291,669 58,436" fill="var(--shape-grey)"/>
    <rect x="444" y="364" width="276" height="273" fill="var(--shape-grey)"/>
    <polygon points="0,899 65,967 0,1040" fill="url(#edgeFade)"/>
    <polygon points="778,1200 928,1047 928,1200" fill="var(--ink)"/>
  </svg>

  <h1 class="block headline">MOVING<br>SOLUTIONS</h1>
  <p class="block tagline">WE ARE HERE TO<br>MOVE YOUR<br>STUFF</p>

  <p class="block ribbon"><span>THE BEST MOVERS</span><span>IN LAS VEGAS</span></p>

  <div class="block we-move condensed">
    <div class="list-head">\-We Move-\</div>
    <div class="list-item">HOMES</div>
    <div class="list-item">APARTMENTS</div>
    <div class="list-item">OFFICES</div>
    <div class="list-item">AND STORAGE...</div>
  </div>

  <div class="block we-provide condensed">
    <div class="list-head">\-We Provide<br>at No Charge-\</div>
    <div class="list-item">BLANKETS</div>
    <div class="list-item">DOLLIES</div>
    <div class="list-item">TOOLS</div>
  </div>

  <p class="block drive">WE<br>WILL<br>DRIVE<br>ANYWHERE<br>WITHIN<br>VEGAS</p>

  <div class="block prices condensed">
    2 MOVERS+TRUCK: $46.99<br>
    3 MOVERS+TRUCK: $66.99<br>
    4 MOVERS+TRUCK: $86.99
  </div>

  <div class="block labor condensed">
    <span class="rate">LABOR ONLY: $19.99/HR PER MOVER</span>
    <span class="note">(CUSTOMER DRIVE THE TRUCK FROM<br>POINT A TO POINT B)</span>
  </div>

  <h2 class="block service">WE PROVIDE<br>PROFESSIONAL<br>MOVING SERVICE</h2>
  <p class="block tasks">PACKING &amp;<br>UNPACKING<br>LOADING &amp;<br>UNLOADING</p>

  <p class="block contact"><span>CALL 702-555-0147</span><span>AVAILABLE 24/7</span></p>
</div>
</body>
</html>
```